Business Card Design Harlow Airflow Systems

The Business will be centred around supply and installation of Ventilation for domestic homes and warehousing/workshops, and will be marketed as a Eco friendly means of reducing your carbon footprint and reducing energy consumption.Our suppliers will provide a range of products that will ventilate roof spaces and later will branch into to air transfer within homes for cooling and heating other rooms of the home etc.I would like to see colours that would be commensurate with the logo provided and yet not dominate the logo.Final design should convey a Diverse , professional but friendly service that will suit client needs

Target Market(s)

Domestic home owners and warehousing/workshop businesses

Industry/Entity Type

Business

Contact Information for Business Card

Company Name: Harlow Airflow Systems Pty Ltd, ABN: 42 817 350 294, Address: 27 Merrow Tunstead W.A 6084, Email: dale@harlowairflowsystems.com.au, Mobile Number: 0451 862 019

Requirements
Nice to have
• A tract art that commensurate of the logo supplied
Should not have
• Font style that opposes logo design

```html
<!DOCTYPE html>
<html lang="en">
<head>
<meta charset="utf-8">
<title>Harlow Airflow Systems – Business Card</title>
<link rel="stylesheet" href="https://fonts.googleapis.com/css2?family=Open+Sans:wght@400;600;700&display=swap">
<style>
  :root {
    --green: #13a84a;
    --maroon: #5a2428;
    --ink: #3a3a3a;
    --rule: #e2e2e2;
    --paper: #ffffff;
    --backdrop: #e9e6e1;
    --card-w: 640px;
    --card-h: 366px;
  }
  * { box-sizing: border-box; margin: 0; padding: 0; }
  html, body {
    width: 1200px; height: 900px; overflow: hidden;
    background: var(--backdrop);
    font-family: "Open Sans", Arial, sans-serif;
  }
  .canvas {
    width: 1200px; height: 900px;
    display: flex; flex-direction: column; align-items: center; justify-content: center;
    gap: 48px;
  }
  .card {
    position: relative;
    width: var(--card-w); height: var(--card-h);
    background: var(--paper);
    box-shadow: 0 6px 18px rgba(0,0,0,.18);
    overflow: hidden;
  }
  .card__swoosh { position: absolute; inset: 0; width: 100%; height: 100%; }
  .brand {
    position: absolute;
    display: flex; align-items: center; gap: 10px;
    color: var(--maroon);
    font-weight: 600;
    white-space: nowrap;
  }
  .brand__mark { background: var(--green); flex: none; }
  .card--front .brand { left: 130px; top: 135px; font-size: 32px; }
  .card--front .brand__mark { width: 20px; height: 20px; }
  .card--back .brand { left: 40px; top: 160px; font-size: 20px; }
  .card--back .brand__mark { width: 13px; height: 13px; }
  .abn {
    position: absolute; left: 40px; top: 120px;
    font-size: 11px; color: var(--ink);
  }
  .divider {
    position: absolute; left: 330px; top: 0; width: 1px; height: 175px;
    background: var(--rule);
  }
  .person { position: absolute; left: 352px; top: 30px; }
  .person__name { font-size: 15px; color: var(--maroon); letter-spacing: .3px; }
  .person__title { font-size: 12px; font-weight: 700; color: var(--ink); margin-left: 18px; }
  .contacts {
    position: absolute; left: 366px; top: 92px;
    list-style: none; font-size: 10.5px; color: var(--ink);
  }
  .contacts li { display: flex; align-items: center; gap: 8px; margin-bottom: 9px; white-space: nowrap; }
  .contacts svg { width: 14px; height: 14px; flex: none; }
</style>
</head>
<body>
<main class="canvas">

  <section class="card card--front" aria-label="Card front">
    <svg class="card__swoosh" viewBox="0 0 640 366" preserveAspectRatio="none" aria-hidden="true">
      <polygon points="0,318 330,292 330,304 0,366" fill="var(--maroon)"/>
      <polygon points="330,292 640,190 640,250 330,304" fill="var(--green)"/>
    </svg>
    <div class="brand"><span class="brand__mark"></span>Harlow Airflow Systems</div>
  </section>

  <section class="card card--back" aria-label="Card back">
    <svg class="card__swoosh" viewBox="0 0 640 366" preserveAspectRatio="none" aria-hidden="true">
      <polygon points="0,318 330,292 330,304 0,366" fill="var(--maroon)"/>
      <polygon points="330,292 640,190 640,250 330,304" fill="var(--green)"/>
    </svg>
    <p class="abn">ABN: 42 817 350 294</p>
    <div class="brand"><span class="brand__mark"></span>Harlow Airflow Systems</div>
    <span class="divider"></span>
    <div class="person">
      <p class="person__name">YOUR NAME</p>
      <p class="person__title">Title</p>
    </div>
    <ul class="contacts">
      <li>
        <svg viewBox="0 0 14 14" aria-hidden="true"><rect width="14" height="14" rx="2" fill="var(--maroon)"/><path d="M7 3a2.6 2.6 0 0 0-2.6 2.6C4.4 8 7 11 7 11s2.6-3 2.6-5.4A2.6 2.6 0 0 0 7 3z" fill="#fff"/><circle cx="7" cy="5.6" r="1" fill="var(--maroon)"/></svg>
        27 Merrow Tunstead W.A 6084
      </li>
      <li>
        <svg viewBox="0 0 14 14" aria-hidden="true"><rect width="14" height="14" rx="2" fill="var(--maroon)"/><path d="M4.3 3.2l1.5-.2.8 2-1 .8a6 6 0 0 0 2.6 2.6l.8-1 2 .8-.2 1.5c-3.6.4-6.9-2.9-6.5-6.5z" fill="#fff"/></svg>
        0451 862 019
      </li>
      <li>
        <svg viewBox="0 0 14 14" aria-hidden="true"><rect width="14" height="14" rx="2" fill="var(--maroon)"/><rect x="3" y="4.2" width="8" height="5.6" fill="#fff"/><path d="M3 4.2l4 3.2 4-3.2" fill="none" stroke="var(--maroon)" stroke-width=".8"/></svg>
        dale@harlowairflowsystems.com.au
      </li>
    </ul>
  </section>

</main>
</body>
</html>
```